Hardcore nerd needs to stand out in a sea of dull Defence business cards

Wombeck Dynamics is a new Australian consulting engineering company that turns research and theory into practical systems. No evangelistic fluff, just mathematics and physics into electronic and optical circuits for consumer products, scientific research or Defence applications.

We already have a recognised logo (provided) which is often dark blue/black on a light background but we're open to other combinations. (Us engineers tend to have limited aesthetic imagination :)

Some of our recent products have included:
* Instrumentation for electrical testing,
* Radar jammers,
* GPS antenna design,
* Satellite tracking systems,
* High power lasers

We're open to both single and double-sided designs - happy to be convinced either way.

P.S. Another group is working on the web page, so - alas - our web site is currently of no use for images/ideas...

Target Market(s)

Engineering managers,
Scientists

Contact Information for Business Card

Dr Martin Folsey
R&D Engineer

martin@wombeckdynamics.com.au
0427 563 201

PO Box XXX (to be confirmed)
Brindlow ACT 2914
Australia

Font styles to use
Serif
Sans Serif

Colors

Designer to choose colors to be used in the design.

Requirements
Must have
• My contact details!
• I've had many (great) "bold and plain" designs submitted already, so feel free to be artistically creative :)
• Happy to take advice re fonts/colours/printability etc.
Nice to have
• I'm not sure if "lists" are more at home on a CV than a business card, but representative services include:
• Applied electromagnetics
• RF and high speed electronics
• Signal and image processing
• Electro-optical and laser systems
• Concept-to-prototype design services
• If you're considering double sided cards, then often measuring/alignment grids/rulers feature on the back of similar cards.
• e.g. https://www.kelvorin.com/newgrouppage9.cfm?objectgroup_id=4183
• https://www.kelvorin.com/newgrouppage9.cfm?objectgroup_ID=4185
• ..or even a "Smith chart" (google will return lots)
• Generic images to represent a capability might work - googling images associated with keyword for each of these areas might help:
• - "passive radar", "phased array", "fdtd", "vircator"
• RF and high speed electronic design
• - "smith chart", "microstrip circuits", "dimensioned drawing", "electronic schematic"
• - "dft", "iir filter"
• - "optical cavity". "laser energy level diagram"
• Background/watermarked images outlines/wireframes/schematics would probably look OK.
Should not have
• If a list of projects/services is provided, it is important not to make the client feel that this is "all" the company can do. Engineering design is a creative discipline (like graphics :)
• Please, no stock "military" snaps like planes, missiles, etc!

```html
<!DOCTYPE html>
<html lang="en">
<head>
<meta charset="utf-8">
<title>Wombeck Dynamics – Business Card</title>
<link href="https://fonts.googleapis.com/css2?family=Poppins:wght@400;500;600;700&display=swap" rel="stylesheet">
<style>
  :root {
    --stage: #e4e4e6;
    --paper: #ffffff;
    --navy: #0a2466;
    --ink-grey: #5d5d62;
    --soft-grey: #a3a3a8;
    --charcoal: #333335;
    --silver: #c9c9cc;
  }
  * { box-sizing: border-box; margin: 0; padding: 0; }
  html, body { width: 1200px; height: 801px; overflow: hidden; }
  body {
    background: var(--stage);
    font-family: "Poppins", sans-serif;
    display: flex;
    align-items: center;
    justify-content: center;
    gap: 50px;
  }
  .card {
    width: 525px;
    height: 300px;
    position: relative;
    overflow: hidden;
    box-shadow: 0 6px 18px rgba(0,0,0,.18);
  }

  /* Front */
  .card-front { background: var(--paper); border-bottom: 3px solid var(--navy); }
  .identity {
    position: absolute;
    left: 40px; top: 110px;
    width: 210px;
    text-align: right;
  }
  .person-name { color: var(--navy); font-weight: 500; font-size: 23px; line-height: 1.1; }
  .person-role { color: var(--soft-grey); font-size: 12px; margin-top: 2px; }
  .divider {
    position: absolute;
    left: 268px; top: 70px;
    width: 1px; height: 100px;
    background: var(--soft-grey);
  }
  .contact {
    position: absolute;
    left: 285px; top: 38px;
    color: var(--ink-grey);
    font-size: 11.5px;
    line-height: 1.4;
  }
  .contact .gap { height: 10px; }
  .services-band {
    position: absolute;
    left: 0; right: 0; top: 190px;
    height: 88px;
    background: var(--navy);
    color: var(--paper);
    font-size: 11.5px;
    line-height: 1.45;
    padding: 14px 0 0 40px;
  }

  /* Back */
  .card-back {
    background: var(--charcoal);
    border-bottom: 2px solid var(--navy);
    display: flex;
    align-items: center;
    justify-content: center;
    gap: 16px;
  }
  .brand-dot {
    width: 70px; height: 70px;
    border-radius: 50%;
    background: var(--silver);
  }
  .brand-name {
    color: var(--silver);
    font-weight: 700;
    font-size: 30px;
    letter-spacing: 1px;
    text-transform: uppercase;
    line-height: 1.05;
  }
</style>
</head>
<body>
  <section class="card card-front">
    <div class="identity">
      <p class="person-name">Dr Martin Folsey</p>
      <p class="person-role">R&amp;D Engineer</p>
    </div>
    <div class="divider"></div>
    <div class="contact">
      <p>PO Box 317</p>
      <p>Brindlow ACT 2914</p>
      <p>Australia</p>
      <div class="gap"></div>
      <p>P. 0427 563 201</p>
      <p>martin@wombeckdynamics.com.au</p>
      <p>www.wombeckdynamics.com.au</p>
    </div>
    <div class="services-band">
      <p>Applied electromagnetics • RF &amp; high speed electronics</p>
      <p>Signal &amp; image processing • Electro-optical &amp; laser systems</p>
      <p>Concept-to-prototype design services</p>
    </div>
  </section>

  <section class="card card-back">
    <span class="brand-dot"></span>
    <p class="brand-name">Wombeck<br>Dynamics</p>
  </section>
</body>
</html>
```